Online Rug Store needs Clearance Banner

Website is: Marvelous Mats and Interiors
You can access it at: www.marvelousmatsandinteriors-example.com and login (top right) with password: plorvat

*** update: When creating banners for my site, you have permission to use images from www.kelvora-example.com, but ONLY for this project. The images/artwork are copyright allowable for use on www.marvelousmatsandinteriors-example.com projects.***

We need a home page banner sized 1000 wide x 500 tall pixels to promote a "Clearance Sale" on rugs. The banner can state:

1. Clearance Sale
2. Now in progress
3. Save an extra 20% with coupon code 'Take20'
4. Ends March 31st
5. Plus Free Shipping and 30 day returns.

We prefer a banner that appears hand-drawn and artistic, not commercially produced. It is OK to use a room scene image, rug images, or just a colored/textured background with text and no images. Your choice.

Flat graphics with no shadows and 3-D effect preferred.
Attached is are 3 logo options, as well as an example banner with handcrafted, artistic styling that we prefer.

Target Market(s)

This should be an eye-catching banner to showcase a very urgent promotion. Consider using colors of red, white, gold, and black to make a strong statement on the home page.

Industry/Entity Type

Home And Garden

Requirements
Must have
• Winner must provide Photoshop editable file format (.psd format) including layers that can be edited.
Nice to have
• Hand-drawn, stenciled, scribbled, artistic graphics and fonts is nice because we sell rugs that are made by hand.
Should not have
• little to no shadowing. Avoid computerized graphics.

```html
<!DOCTYPE html>
<html lang="en">
<head>
<meta charset="utf-8">
<title>Clearance Sale Banner</title>
<link href="https://fonts.googleapis.com/css2?family=Cinzel:wght@400;500&family=Pinyon+Script&display=swap" rel="stylesheet">
<style>
  :root {
    --rug-dark: #1c1410;
    --rug-mid: #5a3a22;
    --rug-warm: #8a6a48;
    --veil: rgba(248, 246, 242, 0.88);
    --ink: #2a1a10;
    --sale-red: #e30b0b;
    --band-red: #f00e0e;
    --white: #ffffff;
  }
  * { margin: 0; padding: 0; box-sizing: border-box; }
  html, body { width: 1200px; height: 600px; overflow: hidden; background: var(--rug-dark); }
  .banner {
    position: relative;
    width: 1200px;
    height: 600px;
    overflow: hidden;
    font-family: "Cinzel", serif;
  }
  .rug-backdrop {
    position: absolute; inset: 0;
    background:
      radial-gradient(ellipse at 50% 50%, var(--rug-warm) 0%, var(--rug-mid) 40%, var(--rug-dark) 85%);
  }
  .title-panel {
    position: absolute;
    left: 0; top: 78px;
    width: 1200px; height: 348px;
    background: var(--veil);
  }
  .brand {
    position: absolute;
    left: 52px; top: 100px;
    display: flex; align-items: center; gap: 12px;
    color: var(--ink);
  }
  .brand-mark {
    width: 46px; height: 46px;
    background: var(--ink);
  }
  .brand-name {
    font-size: 21px; line-height: 24px; font-weight: 400;
    max-width: 260px;
  }
  .headline {
    position: absolute;
    left: 0; top: 138px; width: 1200px;
    text-align: center;
    font-family: "Pinyon Script", cursive;
    font-size: 186px; line-height: 200px;
    color: var(--ink);
    white-space: nowrap;
  }
  .deadline {
    position: absolute;
    left: 0; top: 352px; width: 1200px;
    text-align: center;
    font-size: 50px; line-height: 56px;
    color: var(--sale-red);
  }
  .deadline sup { font-size: 26px; vertical-align: 22px; }
  .offer-band {
    position: absolute;
    left: 0; top: 450px;
    width: 1200px; height: 146px;
    background: var(--band-red);
    color: var(--white);
    text-align: center;
  }
  .offer-code {
    margin-top: 22px;
    font-size: 37px; line-height: 44px;
    letter-spacing: 1px;
  }
  .offer-perks {
    margin-top: 14px;
    font-size: 29px; line-height: 36px;
    letter-spacing: 2px;
    word-spacing: 4px;
  }
  .offer-perks .sep { margin: 0 26px; }
</style>
</head>
<body>
  <main class="banner">
    <div class="rug-backdrop" role="img" aria-label="Close-up of a hand-knotted oriental rug with black field, ivory border and ornate floral medallions"></div>
    <div class="title-panel"></div>
    <div class="brand">
      <span class="brand-mark"></span>
      <span class="brand-name">Marvelous Mats and Interiors</span>
    </div>
    <h1 class="headline">Clearance Sale</h1>
    <p class="deadline">Ends March 31<sup>st</sup></p>
    <section class="offer-band">
      <p class="offer-code">SAVE AN EXTRA 20% WITH COUPON CODE 'TAKE20'</p>
      <p class="offer-perks">FREE SHIPPING<span class="sep">*</span>30 DAY RETURNS<span class="sep">*</span>NOW IN PROGRESS</p>
    </section>
  </main>
</body>
</html>
```